Wordpress Template for Nonprofit Organization
Corvella's Light Foundation
Wordpress Template for Nonprofit Organization - Fund Raising
Creative Brief
Corvella’s Light Foundation, Inc. is a non-profit organization that provides life-sustaining staples to include food, clothing and toiletries to the economically disadvantaged. Our programs include Feeding and Clothing the Homeless, Hunger Outreach, Mentoring Youth, Promoting Literacy, Sustainable Change, and Social Responsibility.
Fund Raising
Below are examples of the design layout I am looking for: http://www.brindlepantry.org http://www.kinfoldcirclenet.org http://www.tamberlodge.org http://www.ourneighborsnestqx.org
Donation Widget or Plugin
Below are examples of the design layout I am looking for:
http://www.brindlepantry.org
http://www.kinfoldcirclenet.org
http://www.tamberlodge.org
http://www.ourneighborsnestqx.org

```html
<!DOCTYPE html>
<html lang="en">
<head>
<meta charset="utf-8">
<title>Corvella's Light Foundation</title>
<link href="https://fonts.googleapis.com/css2?family=Arimo:wght@400;700&display=swap" rel="stylesheet">
<style>
:root{
  --page:#e4e4e4;--white:#fff;--ink:#333;--red:#b3261e;--red-dark:#8e1a14;
  --gold:#d4a35f;--orange-text:#d08a2e;--teal:#2f7590;--teal-head:#4a88a6;
  --green:#7dbf12;--blue:#0aa5d0;--yellow:#ffcc00;--purple:#8e3ea8;--orange:#f47b20;--pink:#e0227f;
}
*{box-sizing:border-box;margin:0;padding:0}
html,body{width:982px;height:1200px;overflow:hidden;background:var(--page)}
body{font-family:"Arimo",Arial,sans-serif;color:var(--ink)}
.stage{position:absolute;left:0;top:0;width:1500px;height:1833px;transform:scale(.654667);transform-origin:0 0;background:var(--page)}
.abs{position:absolute}
a{color:inherit}
.top-strip{left:251px;top:0;width:1000px;height:12px;background:var(--gold)}
.header{left:253px;top:12px;width:996px;height:153px;background:linear-gradient(#fff,#f1f1f1);border-radius:0 0 6px 6px}
.util-links{right:30px;top:10px;font-size:13px;color:#222}
.brand{left:48px;top:36px;display:flex;align-items:center;gap:14px}
.brand-mark{width:84px;height:84px;background:var(--teal);border-radius:8px}
.brand-name{font-size:26px;font-weight:700;color:var(--red);line-height:1.1;width:200px}
.brand-tag{font-size:10px;color:var(--teal);margin-top:4px;font-weight:400}
.connect{right:44px;top:112px;display:flex;align-items:center;gap:7px}
.connect span{font-size:22px;font-weight:700;color:var(--teal);margin-right:6px}
.connect i{width:30px;height:30px;border-radius:6px;display:block}
.nav{left:251px;top:174px;width:1000px;height:62px;background:#fff;border-bottom:8px solid var(--red)}
.nav ul{list-style:none;display:flex;height:54px}
.nav li{font-size:15px;font-weight:700;color:#555;padding:0 17px;display:flex;align-items:center;border-right:1px solid #ddd}
.nav li.current{background:linear-gradient(#c5342a,var(--red-dark));color:#fff;padding:0 32px;border-radius:6px 6px 0 0}
.search{right:10px;top:10px;width:196px;height:34px;border:1px solid #ccc;border-radius:4px;font-size:13px;color:#888;padding:10px 12px;background:#fff;white-space:nowrap;overflow:hidden}
.search svg{position:absolute;right:6px;top:4px;background:#fff}
.tiles{left:264px;top:248px;width:975px;height:428px;display:grid;grid-template-columns:repeat(6,1fr);grid-template-rows:repeat(3,1fr);gap:2px}
.tile{display:flex;align-items:center;justify-content:center;color:#fff;font-size:21px;font-weight:700}
.photo{background:linear-gradient(135deg,#b99e84,#6f7d86)}
.banner{left:255px;top:676px;width:992px;height:44px;background:linear-gradient(var(--red),var(--red-dark));color:#fff;font-size:19px;text-align:center;line-height:44px;letter-spacing:.3px}
.welcome{left:276px;top:742px;width:644px}
.welcome h1{font-size:24px;font-weight:400;display:flex;align-items:center;gap:10px;padding-bottom:12px;border-bottom:1px dotted #bbb}
.welcome h1 i{width:30px;height:30px;background:var(--teal);display:block;border-radius:4px}
.hl-red{color:var(--red)}.hl-gold{color:var(--orange-text)}
.welcome p{font-size:12.5px;line-height:22px;text-align:justify;margin-top:12px}
.welcome p+p{margin-top:22px}
.welcome a{color:var(--red)}
.donate-btn{right:4px;top:262px;background:linear-gradient(#c7372c,var(--red-dark));color:#fff;font-size:16px;padding:9px 13px;border-radius:3px}
.video{left:948px;top:750px;width:280px}
.video h2{font-size:20px;font-weight:700;padding-bottom:10px;border-bottom:1px dotted #bbb}
.player{margin-top:20px;border:1px solid #ddd;background:#fff;padding:5px;height:230px}
.screen{height:192px;background:linear-gradient(135deg,#6e8470,#b08a68 60%,#8a5f4c);position:relative}
.play{position:absolute;left:115px;top:77px;width:30px;height:30px;background:#fff;border-radius:3px}
.play:after{content:"";position:absolute;left:11px;top:8px;border-left:10px solid #222;border-top:7px solid transparent;border-bottom:7px solid transparent}
.bar{position:absolute;left:6px;right:16px;bottom:8px;height:5px;background:#ddd;border-radius:3px}
.bar b{display:block;width:26%;height:100%;background:var(--orange);border-radius:3px}
.controls{display:flex;gap:6px;margin-top:8px;font-size:9px;color:#777}
.controls span{border:1px solid #ddd;border-radius:3px;height:22px;line-height:20px;padding:0 7px}
.panel{top:1077px;width:302px;height:320px;border:1px solid #d8d8d8;background:#fff;overflow:hidden}
.panel h3{height:44px;background:var(--teal-head);color:#fff;font-size:21px;font-weight:400;padding:10px 16px;position:relative}
.panel h3 i{position:absolute;right:8px;top:4px;width:36px;height:36px;border-radius:50%;background:rgba(255,255,255,.85)}
.panel .body{padding:12px 14px;font-size:12.5px;line-height:15.5px}
.mgr-photo{width:128px;height:150px;background:linear-gradient(#5f8a4c,#2b4a8e);float:left;margin:0 10px 0 0}
.teal-link{color:var(--teal);text-decoration:underline}
.news-item{display:flex;gap:14px;padding:4px 0 6px;border-bottom:1px dotted #999;margin-bottom:6px;font-size:12.5px;line-height:15.5px}
.news-item i{flex:none;width:58px;height:58px;border:2px solid #ccc;border-radius:6px;background:var(--teal)}
.panel h4{color:var(--teal);font-size:14.5px;font-weight:400;margin-bottom:6px}
.donate-row{display:flex;gap:18px;margin-top:12px;align-items:center;font-size:12.5px;line-height:17px}
.pill{width:98px;height:28px;border-radius:14px;background:linear-gradient(#ffd45a,#f2a100);color:#1f3e7a;font-weight:700;font-size:15px;text-align:center;line-height:28px}
.cards{display:flex;gap:3px;margin-top:8px}.cards i{width:23px;height:13px;background:#bbb;display:block}
.thanks{top:1411px;height:150px;border:1px solid #d8d8d8;background:#fff;padding:12px 15px}
.thanks h3{font-size:18px;font-weight:400;color:#111}
.arrows{position:absolute;right:20px;top:14px;display:flex;gap:2px}
.arrows i{width:17px;height:17px;background:var(--teal-head);display:block}
.thumbs{display:flex;gap:14px;margin-top:14px}
.thumb{width:134px;height:92px;border:1px solid #ddd;padding:4px;background:#fff}
.thumb i{display:block;width:100%;height:100%;background:linear-gradient(135deg,#c0a08a,#4f6fa0)}
.sponsor{width:134px;height:92px;border:1px solid #ddd;display:flex;align-items:center;justify-content:center;font-size:14px;font-weight:700;color:#555}
.footer{left:251px;top:1578px;width:1000px;height:210px;background:linear-gradient(var(--red),#9e1f18);border-radius:8px 8px 0 0;color:#fff}
.fcol{top:38px;font-size:13px;line-height:18px}
.fcol h5{font-size:15px;font-weight:700;margin-bottom:22px}
.fsep{top:36px;width:0;height:150px;border-left:1px dotted rgba(255,255,255,.5)}
.map{left:765px;top:56px;width:198px;height:120px;border:3px solid #fff;background:linear-gradient(135deg,#ece4cf,#d9e3cc)}
.bottom{left:251px;top:1787px;width:1000px;height:46px;background:var(--gold);color:#fff;font-size:13px;padding:16px 24px}
.bottom .social{position:absolute;right:20px;top:10px;display:flex;gap:6px;align-items:center;font-weight:700}
.bottom .social i{width:26px;height:26px;border-radius:50%;background:rgba(255,255,255,.85);display:block}
</style>
</head>
<body>
<div class="stage">
  <div class="abs top-strip"></div>
  <header class="abs header">
    <div class="abs util-links">Donate | Foundation Donors | Volunteer | Media Partner | Press Releases | News</div>
    <div class="abs brand">
      <div class="brand-mark"></div>
      <div class="brand-name">CORVELLA'S LIGHT FOUNDATION<div class="brand-tag">serving people, changing lives</div></div>
    </div>
    <div class="abs connect" aria-label="Social links"><span>Connect With Us</span>
      <i style="background:#3b5998"></i><i style="background:#29a9e1"></i><i style="background:#0e76a8"></i><i style="background:#c4302b"></i><i style="background:#f26522"></i></div>
  </header>
  <nav class="abs nav">
    <ul><li class="current">HOME</li><li>OUR PROGRAMS</li><li>ABOUT THE FOUNDER</li><li>DONATIONS</li><li>NEWS</li><li style="border:0">CONTACT US</li></ul>
    <div class="abs search">Search Brightline Electric
      <svg width="30" height="26" viewBox="0 0 30 26"><circle cx="11" cy="11" r="7" fill="none" stroke="#c4302b" stroke-width="3"/><line x1="16" y1="16" x2="26" y2="23" stroke="#c4302b" stroke-width="4"/></svg></div>
  </nav>
  <section class="abs tiles">
    <div class="photo" role="img" aria-label="Child with donation box"></div>
    <div class="tile" style="background:var(--green)">Love</div>
    <div class="photo" role="img" aria-label="Woman at clothing bank"></div>
    <div class="tile" style="background:var(--blue)">Joy</div>
    <div class="photo" role="img" aria-label="Volunteers with donations box"></div>
    <div class="tile" style="background:var(--yellow)">Peace</div>
    <div class="tile" style="background:var(--purple)">Longsuffering</div>
    <div class="photo" role="img" aria-label="Young volunteer outdoors"></div>
    <div class="tile" style="background:var(--orange)">Gentleness</div>
    <div class="photo" role="img" aria-label="Volunteers at bake sale"></div>
    <div class="tile" style="background:var(--pink)">Goodness</div>
    <div class="photo" role="img" aria-label="Volunteers serving food"></div>
    <div class="photo" role="img" aria-label="Donation box of clothes"></div>
    <div class="tile" style="background:var(--yellow)">Faith</div>
    <div class="photo" role="img" aria-label="Food donation box"></div>
    <div class="tile" style="background:var(--green)">Meekness</div>
    <div class="photo" role="img" aria-label="Kids at food drive"></div>
    <div class="tile" style="background:var(--blue)">Temperance</div>
  </section>
  <div class="abs banner"><b>Corvella's</b> Light Foundation (A Non-Profit Organization) &nbsp;- &nbsp;<b>Serving People, Changing Lives</b></div>

  <section class="abs welcome">
    <h1><i></i><span>Welcome to <span class="hl-red">Corvella's</span> <span class="hl-gold">Light</span> Foundation Inc.</span></h1>
    <p><b>Corvella</b> means "Light Shared With All". Our goal is simply to help as many people as we possibly can by spreading a message of hope through service.lectus a arcu consequat dignissim eu vel tortor. Nullam enim lorem, luctus ac ipsum vestibulum, blandit luctus ligula. Phasellus tincidunt lacinia rutrum. Donec orci est, luctus vitae mi convallis, cursus posuere ante. Vestibulum feugiat scelerisque sapien, quis porttitor elit gravida eu. Vestibulum ante ipsum primis in faucibus orci luctus et ultrices posuerverris, simet tempor nisl.</p>
    <p>Join us in our mission of helping fund Lorem ipsum dolor sit amet, consectetur adipiscing elit. Vivamus sed lorem et nibh imperdiet dictum. Ut ornare ipsum sit amet est lacinia, sit ame. Please read about our mission on the <a href="#">About Us</a> page or see how you can <a href="#">donate</a> to Secure the people.</p>
    <div class="abs donate-btn">Click Here to Donate Us</div>
  </section>

  <section class="abs video">
    <h2><span class="hl-red">Video</span> <span class="hl-gold">Presentation</span></h2>
    <div class="player">
      <div class="screen" role="img" aria-label="Video still of volunteers handing out clothes"><div class="play"></div><div class="bar"><b></b></div></div>
      <div class="controls"><span>▶</span><span>2:33 / 9:49</span><span>🔈 ▮▮▮</span><span style="margin-left:14px">SHARE ▾</span><span>⤢</span></div>
    </div>
  </section>

  <section class="abs panel" style="left:276px">
    <h3>Management Team<i></i></h3>
    <div class="body">
      <p style="text-align:justify">Marla Denton is Founder &amp; Director of Corvella's Light Foundation, a nonprofit organization that takes a life-saving and hope-giving message of care to the world. Vivamus eu tellus nulla.</p>
      <div style="margin-top:12px">
        <div class="mgr-photo" role="img" aria-label="Young volunteer in team shirt"></div>
        <p>Maeceas cursus purus conllis, convallis dolor uteuiat tellut mollis vel quad conean sit amet ipsum ipsumlla facilisi. Vivmus eu tellus nulla. d vitae augue ac diam blans a sed nunc.</p>
        <p class="teal-link" style="margin-top:4px">Click here to Read<br>More about Pelwintra</p>
      </div>
    </div>
  </section>

  <section class="abs panel" style="left:601px">
    <h3>Latest News<i></i></h3>
    <div class="body">
      <div class="news-item"><i></i><p>Corvella's Light Foundation cursus purus conv convallis dolor ut, feugit tollis vem id consectetm blandit sodales sed nunc.</p></div>
      <div class="news-item"><i></i><p>Corvella's Light Foundation cursus purus conv convallis dolor ut, feugit tollis vem id consectetm blandit sodales sed nunc.</p></div>
      <div class="news-item"><i></i><p>Corvella's Light Foundation cursus purus conv convallis dolor ut, feugit tollis vem id consectetm blandit sodales sed nunc.</p></div>
      <p class="teal-link" style="text-align:right">Click here to View more</p>
    </div>
  </section>

  <section class="abs panel" style="left:926px">
    <h3>How To Donate<i></i></h3>
    <div class="body">
      <h4>Help Make A Difference</h4>
      <p style="text-align:justify">Over the last decade many great advancements have been made in the field of Quisque arcu justo, posuere ut nulla ut, interdum cursus lerdum c lectu pretium magna nec feliretium, sed ultrices nibh elementum. Nullam eu lectus a arc consequat dignissim eu vel tortor. Nullam enim lorem, luctus ac ipsum vestibulum, blandit luctusli tincidunt lacinia rutrum, sed ultrices nibh elemelam eu lectus a arcu consequat dignissim euel tortor.</p>
      <div class="donate-row">
        <div><div class="pill">Donate</div><div class="cards" aria-label="Accepted payment cards"><i></i><i></i><i></i><i></i></div></div>
        <p>Click the <span style="color:var(--teal);font-size:15px">"Donate"</span> button left and specify a donation amount:</p>
      </div>
    </div>
  </section>

  <section class="abs thanks" style="left:276px;width:461px">
    <h3>Thank You to our Volunteers</h3>
    <div class="arrows"><i></i><i></i></div>
    <div class="thumbs">
      <div class="thumb"><i role="img" aria-label="Volunteers at bake sale"></i></div>
      <div class="thumb"><i role="img" aria-label="Young volunteers outdoors"></i></div>
      <div class="thumb"><i role="img" aria-label="Kids at food drive"></i></div>
    </div>
  </section>

  <section class="abs thanks" style="left:749px;width:460px">
    <h3>Thank You to our Platinum Sponsors</h3>
    <div class="arrows"><i></i><i></i></div>
    <div class="thumbs">
      <div class="sponsor">Vantora Trails</div>
      <div class="sponsor">Qeld Solutions</div>
      <div class="sponsor">Gatherly Events</div>
    </div>
  </section>

  <footer class="abs footer">
    <div class="abs fcol" style="left:27px"><h5>Quick links</h5>Home<br>Our Programs<br>About Founder<br>Donations<br>News/Events<br>Contact Us</div>
    <div class="abs fsep" style="left:137px"></div>
    <div class="abs fcol" style="left:177px;top:40px"><h5>Our Programs</h5>Hunger Outreach<br>Prison Outreach<br>Homeless Outreach<br>Evangelistic Crusades<br>Youth Crusades<br>Senior/Elderly Outreach</div>
    <div class="abs fsep" style="left:348px"></div>
    <div class="abs fcol" style="left:385px;top:40px"><h5>Our Programs</h5>Need Shelter?<br>Need Cloth?<br>Need Food?<br>Terms &amp; Conditions<br>Literacy Programs<br>Find Us</div>
    <div class="abs fsep" style="left:533px"></div>
    <div class="abs fcol" style="left:568px;line-height:20px"><h5>Contact Us</h5><b>Corvella's Light Foundation</b><br>Phone: &nbsp;<b>1.555.010.2231</b><br>Toll-Free: <b>1.555.010.2231</b><br>@LightToHearts (Social)<br>info@corvellaslight.org</div>
    <div class="abs map" role="img" aria-label="Street map of the foundation location"></div>
  </footer>
  <div class="abs bottom">© Copyright 2013 <b>Corvella's Light Foundation, Inc.</b> All right reserved
    <div class="social">Connected with Us&nbsp;<i></i><i></i><i></i><i></i><i></i></div>
  </div>
</div>
</body>
</html>
```